Specialized Personal Trainer Needs a Business Card Design

I need a business card design for my personal training business called Tall Oak Fitness. I have my Human Kinetics degree in Exercise Science from the Halvern Ridge University as well as an extra certification from NBEP (National Board of Exercise Practice). I work as a Cardiac Rehab Exercise Specialist and personal trainer giving specialized exercise prescriptions to those that have different heart conditions as well as work with the general population in weight loss, strength and conditioning, getting/staying fit.
Updates

I decided that I wanted a logo (as I did not have one before I submitted my project for a business card) so I am submitting a project to get a logo done and then I will decide on a business card, hopefully being able to use one of the designs already submitted.  My apologies for doing this backwards.  I am new to this so I appreciate your patience.

Thank you.

Hi, I have just created a project for a logo design (I realized I needed a logo and I should've done that first..oops!), please feel free to participate.  Once I receive a logo I like I will finalize my business card project and hopefully incorporate it into one of your business card designs. 

Thank you!

Target Market(s)

Business professionals

Industry/Entity Type

Personal Trainer

Requirements
Must have
• My name with my info:
Celia R. Dunhill (BHK)
NBEP Certified Clinical Exercise Specialist & Personal Trainer
celia.dunhill@talloakfitness.example
Cell: 604-358-4170

Please make it double sided.
Nice to have
• An image that represents cardiac and general fitness training.

```html
<!DOCTYPE html>
<html lang="en">
<head>
<meta charset="utf-8">
<title>Tall Oak Fitness – Business Card</title>
<link rel="stylesheet" href="https://fonts.googleapis.com/css2?family=Oswald:wght@200;300&family=Inter:wght@300&display=swap">
<style>
  :root {
    --paper: #ffffff;
    --ink: #000000;
    --brand-red: #f20000;
    --reverse: #ffffff;
  }
  html, body {
    margin: 0;
    padding: 0;
    width: 1200px;
    height: 866px;
    overflow: hidden;
    background: var(--paper);
  }
  .canvas {
    position: relative;
    width: 1200px;
    height: 866px;
  }
  .card-front {
    position: absolute;
    left: 320px;
    top: 3px;
    width: 582px;
    height: 369px;
    box-sizing: border-box;
    border: 10px solid var(--ink);
    background: var(--paper);
  }
  .brand-dot {
    position: absolute;
    left: 36px;
    top: 75px;
    width: 200px;
    height: 200px;
    border-radius: 50%;
    background: var(--brand-red);
  }
  .wordmark {
    position: absolute;
    left: 281px;
    top: 20px;
    margin: 0;
    font-family: "Oswald", sans-serif;
    font-weight: 200;
    color: var(--ink);
    text-transform: uppercase;
    line-height: 0.98;
    letter-spacing: 1px;
  }
  .wordmark span { display: block; }
  .wordmark .line-lead { font-size: 132px; line-height: 1.0; }
  .wordmark .line-mid,
  .wordmark .line-end { font-size: 98px; }

  .card-back {
    position: absolute;
    left: 320px;
    top: 395px;
    width: 582px;
    height: 375px;
    background: var(--brand-red);
    color: var(--reverse);
  }
  .back-brand {
    position: absolute;
    left: 240px;
    top: 118px;
    display: flex;
    align-items: center;
    gap: 8px;
    font-family: "Inter", sans-serif;
    font-weight: 300;
    font-size: 34px;
    line-height: 1;
  }
  .back-brand .mark {
    width: 30px;
    height: 30px;
    border-radius: 50%;
    background: var(--ink);
  }
  .contact {
    position: absolute;
    left: 286px;
    top: 176px;
    margin: 0;
    padding: 0;
    list-style: none;
    font-family: "Inter", sans-serif;
    font-weight: 300;
    font-size: 15px;
    line-height: 39px;
    text-transform: uppercase;
  }
  .contact .email { text-transform: none; }
  .contact .phone { text-transform: none; }
</style>
</head>
<body>
  <main class="canvas">
    <section class="card-front" aria-label="Card front">
      <div class="brand-dot" aria-hidden="true"></div>
      <h1 class="wordmark">
        <span class="line-lead">Tall</span>
        <span class="line-mid">Oak</span>
        <span class="line-end">Fitness</span>
      </h1>
    </section>

    <section class="card-back" aria-label="Card back">
      <div class="back-brand">
        <span class="mark" aria-hidden="true"></span>
        <span class="initials">TOF</span>
      </div>
      <ul class="contact">
        <li class="name">Celia R. Dunhill (BHK)</li>
        <li class="credential">NBEP Certified Clinical Exercise</li>
        <li class="role">Specialist &amp; Personal Trainer</li>
        <li class="email">celia.dunhill@talloakfitness.example</li>
        <li class="phone">c: 604-358-4170</li>
      </ul>
    </section>
  </main>
</body>
</html>
```